KORBALT

The business want a professional looking business card. We have a scetch we will add but want the extra upgrade, and would like more suggestions for variations of our business cards.

```html
<!DOCTYPE html>
<html lang="en">
<head>
<meta charset="utf-8">
<title>NEWEDEN – Business Card</title>
<link rel="stylesheet" href="https://fonts.googleapis.com/css2?family=Noto+Sans:wght@400;500;600;700&family=Montserrat:wght@400;500&display=swap">
<style>
  :root {
    --page-bg: #e9eaec;
    --card-white: #fbfbfb;
    --navy: #15294a;
    --navy-deep: #132a4f;
    --ink: #1b2436;
    --blue-bright: #1b5fae;
    --blue-mid: #1f4f93;
    --silver: #d9dde3;
    --line-light: #e6ebf2;
  }
  * { box-sizing: border-box; margin: 0; padding: 0; }
  html, body { width: 1200px; height: 940px; overflow: hidden; }
  body {
    background: var(--page-bg);
    font-family: "Noto Sans", Arial, sans-serif;
    color: var(--ink);
    position: relative;
  }
  .card {
    position: absolute;
    left: 243px;
    width: 714px;
    height: 385px;
    overflow: hidden;
  }
  .card--front { top: 66px; background: var(--card-white); }
  .card--back { top: 489px; background: radial-gradient(circle at 30% 40%, #1b3662 0%, var(--navy-deep) 70%); }

  /* brand block */
  .brand {
    position: absolute;
    left: 56px;
    top: 118px;
    width: 260px;
    display: flex;
    align-items: center;
    justify-content: center;
    gap: 12px;
  }
  .brand__dot {
    width: 22px; height: 22px; border-radius: 50%;
    background: var(--navy);
  }
  .brand__name {
    font-weight: 700;
    font-size: 40px;
    letter-spacing: 1px;
    color: var(--navy);
  }
  .tagline {
    position: absolute;
    left: 53px;
    top: 290px;
    font-family: "Montserrat", Arial, sans-serif;
    font-size: 13.5px;
    letter-spacing: 4.3px;
    line-height: 22px;
    color: var(--navy);
  }
  .divider {
    position: absolute;
    left: 360px; top: 40px;
    width: 2px; height: 285px;
    background: var(--navy);
  }
  .person {
    position: absolute;
    left: 392px; top: 36px;
  }
  .person__name { font-size: 31px; font-weight: 600; color: var(--navy); line-height: 1.2; }
  .person__role { font-size: 19.5px; color: var(--ink); margin-top: 4px; }
  .contacts {
    position: absolute;
    left: 392px; top: 138px;
    list-style: none;
  }
  .contacts li {
    display: flex;
    align-items: flex-start;
    font-size: 20px;
    line-height: 27px;
    margin-bottom: 8px;
  }
  .contacts li.contact--web { margin-top: 4px; }
  .contacts svg {
    width: 22px; height: 22px;
    margin: 2px 24px 0 0;
    flex: none;
    fill: var(--navy);
  }

  .band {
    position: absolute;
    left: 0; bottom: 0;
    width: 714px; height: 26px;
  }
  .card--front .band { height: 34px; }

  .motto {
    position: absolute;
    left: 78px; top: 155px;
    font-family: "Montserrat", Arial, sans-serif;
    font-size: 20px;
    letter-spacing: 5.4px;
    line-height: 35px;
    color: var(--line-light);
  }
  .motto__rule {
    position: absolute;
    left: 190px; top: 238px;
    width: 56px; height: 2px;
    background: var(--line-light);
  }
  .back-decor {
    position: absolute;
    left: 440px; top: 20px;
    width: 380px; height: 380px;
    border-radius: 50%;
    background: radial-gradient(circle at 40% 40%, rgba(40,100,180,0.35), rgba(30,80,160,0.15));
  }
</style>
</head>
<body>

<section class="card card--front" aria-label="Business card front">
  <div class="brand">
    <span class="brand__dot"></span>
    <span class="brand__name">NEWEDEN</span>
  </div>
  <p class="tagline">PRECISION COMPONENTS<br>FOR A GLOBAL INDUSTRY</p>

  <div class="divider"></div>

  <div class="person">
    <h1 class="person__name">Daniel Hart</h1>
    <p class="person__role">Managing Director</p>
  </div>

  <ul class="contacts">
    <li>
      <svg viewBox="0 0 24 24" aria-hidden="true"><path d="M6.6 10.8a15.1 15.1 0 0 0 6.6 6.6l2.2-2.2a1 1 0 0 1 1-.25 11.4 11.4 0 0 0 3.6.57 1 1 0 0 1 1 1V20a1 1 0 0 1-1 1A17 17 0 0 1 3 4a1 1 0 0 1 1-1h3.5a1 1 0 0 1 1 1c0 1.25.2 2.45.57 3.57a1 1 0 0 1-.25 1z"/></svg>
      +44 7700 900456
    </li>
    <li>
      <svg viewBox="0 0 24 24" aria-hidden="true"><path d="M2 5h20v14H2zm2 2v.3l8 5.2 8-5.2V7zm0 2.7V17h16V9.7l-8 5.2z"/></svg>
      daniel.hart@neweden.com
    </li>
    <li>
      <svg viewBox="0 0 24 24" aria-hidden="true"><path d="M12 2a7 7 0 0 0-7 7c0 5.2 7 13 7 13s7-7.8 7-13a7 7 0 0 0-7-7zm0 9.5A2.5 2.5 0 1 1 12 6.5a2.5 2.5 0 0 1 0 5z"/></svg>
      <span>Unit 9, Meridian Park<br>Coventry, CV3 4XY<br>United Kingdom</span>
    </li>
    <li class="contact--web">
      <svg viewBox="0 0 24 24" aria-hidden="true"><path d="M12 2a10 10 0 1 0 0 20 10 10 0 0 0 0-20zm7.9 9h-3.5a15 15 0 0 0-1.3-6.1A8 8 0 0 1 19.9 11zM12 4c.9 1.2 2.2 3.6 2.4 7H9.6c.2-3.4 1.5-5.8 2.4-7zM8.9 4.9A15 15 0 0 0 7.6 11H4.1a8 8 0 0 1 4.8-6.1zM4.1 13h3.5a15 15 0 0 0 1.3 6.1A8 8 0 0 1 4.1 13zM12 20c-.9-1.2-2.2-3.6-2.4-7h4.8c-.2 3.4-1.5 5.8-2.4 7zm3.1-.9a15 15 0 0 0 1.3-6.1h3.5a8 8 0 0 1-4.8 6.1z"/></svg>
      www.neweden.com
    </li>
  </ul>

  <svg class="band" viewBox="0 0 714 34" preserveAspectRatio="none" aria-hidden="true">
    <defs>
      <linearGradient id="bandBlueFront" x1="0" x2="1">
        <stop offset="0" stop-color="#1f56a0"/>
        <stop offset="1" stop-color="#1b62b3"/>
      </linearGradient>
    </defs>
    <rect x="0" y="10" width="560" height="24" fill="url(#bandBlueFront)"/>
    <polygon points="536,34 568,4 588,4 556,34" fill="var(--silver)"/>
    <polygon points="562,34 594,0 714,0 714,34" fill="var(--navy-deep)"/>
  </svg>
</section>

<section class="card card--back" aria-label="Business card back">
  <div class="back-decor" role="img" aria-label="Large faint brand emblem area"></div>
  <p class="motto">GLOBAL REACH<br>LOCAL COMMITMENT</p>
  <div class="motto__rule"></div>

  <svg class="band" viewBox="0 0 714 30" preserveAspectRatio="none" aria-hidden="true" style="height:30px">
    <defs>
      <linearGradient id="bandBlueBack" x1="0" x2="1">
        <stop offset="0" stop-color="#1d4f96"/>
        <stop offset="1" stop-color="#1b62b3"/>
      </linearGradient>
    </defs>
    <rect x="0" y="0" width="714" height="30" fill="var(--navy-deep)"/>
    <rect x="0" y="0" width="490" height="30" fill="url(#bandBlueBack)"/>
    <polygon points="470,30 500,0 526,0 496,30" fill="var(--silver)"/>
  </svg>
</section>

</body>
</html>
```